Brochure Design Project

Architectural photography and virtual tour provider for local and national real estate markets. You can use my website for design and image needs. www.larchviewhomeshots.com

```html
<!DOCTYPE html>
<html lang="en">
<head>
<meta charset="utf-8">
<title>Larchview Home Shots – Trifold Brochure</title>
<link href="https://fonts.googleapis.com/css2?family=Oswald:wght@500;600;700&family=Open+Sans:ital,wght@0,400;0,600;0,700;1,400&display=swap" rel="stylesheet">
<style>
:root{
  --stage:#545454;
  --blue:#1c58a8;
  --blue-deep:#154896;
  --navy:#16489a;
  --green:#3cb54a;
  --orange:#f29a1f;
  --ink:#333;
  --paper:#fff;
  --mist:#ececec;
}
*{box-sizing:border-box;margin:0;padding:0}
html,body{width:1200px;height:1200px;overflow:hidden;background:var(--stage);font-family:"Open Sans",sans-serif;color:var(--ink)}
.spread{position:absolute;left:252px;width:696px;height:540px;background:var(--paper);overflow:hidden}
.spread--outside{top:50px}
.spread--inside{top:611px}
.panel{position:absolute;top:0;width:232px;height:540px;overflow:hidden}
.p1{left:0}.p2{left:232px}.p3{left:464px}
.photo{position:absolute;left:0;width:100%}
.heading{font-family:"Oswald",sans-serif;font-weight:700;line-height:1;letter-spacing:.2px}
.rule{display:block;width:30px;height:3px;background:var(--orange);margin-top:5px}

/* outside: prep panel */
.prep{background:linear-gradient(90deg,#fff 0%,#fff 55%,#dedede 100%)}
.prep .heading{position:absolute;left:14px;top:14px;font-size:25px}
.prep .heading .blue{color:var(--blue)}
.prep .heading .green{color:var(--green)}
.prep .rule{margin-left:124px}
.checklist{position:absolute;left:20px;top:110px;width:204px;list-style:none;font-size:8.6px;line-height:12.4px}
.checklist li{position:relative;padding-left:13px;margin-bottom:3.2px;text-align:justify}
.checklist li::before{content:"";position:absolute;left:1px;top:4px;width:5px;height:5px;border-radius:50%;border:1.3px solid var(--green)}

/* logo block */
.brand-head{position:absolute;left:0;top:0;width:100%;height:83px;background:linear-gradient(180deg,#fff,#f1f1f1)}
.brand{position:absolute;display:flex;align-items:center;gap:6px}
.brand-mark{width:14px;height:14px;background:var(--blue)}
.brand-name{font-weight:600;color:#222}
.brand-tag{position:absolute;font-size:5px;color:#444}
.brand-former{position:absolute;font-size:5.6px;color:#555;letter-spacing:.3px}

.swoosh{position:absolute;left:0;top:0}
.partners{position:absolute;left:20px;top:354px;width:190px;height:66px;background:#fff;border-radius:8px;box-shadow:0 2px 4px rgba(0,0,0,.15)}
.partners span{position:absolute;background:#d9dde3;border-radius:3px}
.quote{position:absolute;left:14px;top:430px;width:206px;color:#fff;font-size:7.2px;font-style:italic;line-height:10px}
.quote small{display:block;font-size:5.4px}
.socials{position:absolute;left:0;top:478px;width:100%;display:flex;justify-content:center;gap:6px}
.socials span{width:17px;height:17px;border-radius:50%;background:var(--orange)}
.url-pill{position:absolute;left:42px;top:503px;width:148px;height:16px;border-radius:8px;background:var(--green);color:#fff;font-size:8.4px;line-height:16px;text-align:center}

.selling{position:absolute;left:12px;top:390px;list-style:none}
.selling li{display:flex;align-items:center;gap:4px;font-family:"Oswald",sans-serif;font-weight:600;color:#fff;font-size:15.5px;height:27px}

/* inside */
.top-band{position:absolute;left:0;top:0;height:11px;width:100%}
.about .heading{position:absolute;left:15px;top:15px;font-size:26px;color:var(--blue)}
.feature{position:absolute;left:14px;width:210px}
.feature h3{font-family:"Oswald",sans-serif;font-weight:600;font-size:11.4px;color:var(--orange);display:flex;align-items:center;gap:5px}
.feature p,.feature li{font-size:8.4px;line-height:12.4px;color:#222}
.feature p{padding-left:17px;margin-top:3px}
.feature ul{list-style:none;margin-top:3px;padding-left:25px}
.feature li{position:relative;margin-bottom:3px}
.feature li::before{content:"";position:absolute;left:-10px;top:4px;width:4.6px;height:4.6px;border-radius:50%;border:1.3px solid var(--green)}

.best .heading{position:absolute;left:12px;top:15px;font-size:26px;color:var(--navy)}
.best .heading .green{color:var(--green)}
.body-copy{position:absolute;left:12px;width:208px;font-size:8.5px;line-height:12.4px;text-align:justify}
.howto{position:absolute;left:12px;top:274px;font-family:"Oswald",sans-serif;font-weight:600;color:var(--orange);font-size:13.5px;display:flex;align-items:center;gap:6px}

.tech h3{position:absolute;left:10px;top:28px;font-family:"Oswald",sans-serif;font-weight:600;color:var(--orange);font-size:14.5px;display:flex;align-items:center;gap:6px}
.ba-label{position:absolute;top:8px;height:17px;padding:0 8px;border-radius:9px;background:#fff;font-family:"Oswald",sans-serif;font-weight:500;font-size:11px;line-height:17px;color:#222}

.includes{position:absolute;left:232px;top:0;width:464px;height:540px}
.includes-title{position:absolute;left:0;top:426px;width:464px;display:flex;align-items:center;justify-content:center;gap:14px;font-family:"Oswald",sans-serif;font-weight:600;color:#fff;font-size:14px}
.includes-title i{display:block;width:78px;height:1.5px;background:#fff}
.includes-list{position:absolute;top:455px;list-style:none}
.includes-list li{display:flex;align-items:center;gap:9px;height:25px;color:#fff;font-size:8.6px;font-weight:600}
</style>
</head>
<body>

<!-- OUTSIDE SPREAD -->
<section class="spread spread--outside">
  <div class="panel p1 prep">
    <h1 class="heading"><span class="blue">PREPARE<br>YOUR HOME FOR</span><br><span class="green">PHOTO SHOOT</span><span class="rule"></span></h1>
    <ul class="checklist">
      <li>Thoroughly clean whole house (vacuum carpet, mop floors, clean counter tops, clean windows)</li>
      <li>Turn all overhead lights and lamps ON</li>
      <li>Use bulbs of the same temperature (ALL incandescent or ALL compact fluorescent)</li>
      <li>Replace all burned out light bulbs</li>
      <li>Turn all ceiling fans OFF</li>
      <li>Turn all TVs OFF</li>
      <li>Turn all computer screens OFF</li>
      <li>Open blinds/window treatments to let in outside light</li>
      <li>Remove personal photographs (or replace with general landscape/object photographs)</li>
      <li>Make all beds</li>
      <li>Remove small floor rugs to reveal actual flooring</li>
      <li>Place all shoes/jackets in closet</li>
    </ul>
    <div class="photo" style="top:382px;height:158px;background:linear-gradient(180deg,#c9d3e0 0%,#9aa9b8 35%,#6f9fb0 60%,#7a6a5a 100%)" role="img" aria-label="Backyard pool with palm trees and lounge chairs"></div>
  </div>

  <div class="panel p2">
    <div class="brand-head">
      <div class="brand" style="left:56px;top:26px"><span class="brand-mark"></span><span class="brand-name" style="font-size:9.6px">Larchview Home Shots</span></div>
      <span class="brand-tag" style="left:150px;top:42px">Become noticed...</span>
      <span class="brand-former" style="left:90px;top:59px">formerly Silver Basin Home Tours</span>
    </div>
    <div class="photo" style="top:83px;height:290px;background:linear-gradient(160deg,#6a4b34 0%,#b7845a 35%,#3c5b86 60%,#6b3b22 100%)" role="img" aria-label="Dining room with chandelier and city view at dusk"></div>
  </div>

  <div class="panel p3">
    <div class="brand-head">
      <div class="brand" style="left:22px;top:22px"><span class="brand-mark" style="width:18px;height:18px"></span><span class="brand-name" style="font-size:12.6px">Larchview Home Shots</span></div>
      <span class="brand-tag" style="left:152px;top:40px;font-size:6px">Become noticed...</span>
      <span class="brand-former" style="left:69px;top:65px;font-size:6.8px">formerly Silver Basin Home Tours</span>
    </div>
    <div class="photo" style="top:83px;height:290px;background:linear-gradient(180deg,#1f3e72 0%,#6b6a6e 40%,#2f8fc6 70%,#4a5a66 100%)" role="img" aria-label="Modern home with lit pool at twilight"></div>
  </div>

  <svg class="swoosh" style="left:232px" width="464" height="540" viewBox="0 0 464 540" aria-hidden="true">
    <path d="M0,342 Q116,300 232,354 Q372,384 464,322 L464,540 L0,540Z" fill="var(--green)"/>
    <path d="M0,350 Q116,310 232,362 Q372,392 464,330 L464,540 L0,540Z" fill="var(--orange)"/>
    <path d="M0,355 Q116,316 232,366 Q372,396 464,335 L464,540 L0,540Z" fill="var(--blue)"/>
  </svg>

  <div class="panel p2" style="pointer-events:none">
    <div class="partners">
      <span style="left:16px;top:8px;width:20px;height:20px"></span>
      <span style="left:60px;top:12px;width:56px;height:12px"></span>
      <span style="left:130px;top:10px;width:46px;height:16px"></span>
      <span style="left:22px;top:38px;width:62px;height:18px"></span>
      <span style="left:106px;top:36px;width:60px;height:22px"></span>
    </div>
    <p class="quote">“Best virtual tour provider in town. Mr. Halvorsen and his team are the best!”<br>-DANA WHITFIELD<small>Crestline Realty Group</small></p>
    <div class="socials"><span></span><span></span><span></span><span></span></div>
    <div class="url-pill">www.larchviewhomeshots.com</div>
  </div>

  <div class="panel p3">
    <ul class="selling">
      <li><svg width="22" height="18" viewBox="0 0 22 18"><path d="M2,9 L8,15 L20,2" fill="none" stroke="var(--green)" stroke-width="3.4" stroke-linecap="round"/></svg>Quality YOU CAN SEE</li>
      <li><svg width="22" height="18" viewBox="0 0 22 18"><path d="M2,9 L8,15 L20,2" fill="none" stroke="var(--green)" stroke-width="3.4" stroke-linecap="round"/></svg>Professional PHOTOGRAPHERS</li>
      <li><svg width="22" height="18" viewBox="0 0 22 18"><path d="M2,9 L8,15 L20,2" fill="none" stroke="var(--green)" stroke-width="3.4" stroke-linecap="round"/></svg>Latest DRONE TECHNOLOGY</li>
      <li><svg width="22" height="18" viewBox="0 0 22 18"><path d="M2,9 L8,15 L20,2" fill="none" stroke="var(--green)" stroke-width="3.4" stroke-linecap="round"/></svg>Tours STARTING AT $105</li>
    </ul>
    <div class="url-pill">www.larchviewhomeshots.com</div>
  </div>
</section>

<!-- INSIDE SPREAD -->
<section class="spread spread--inside">
  <div class="panel p1 about">
    <div class="top-band" style="background:var(--green)"></div>
    <h2 class="heading">ABOUT US<span class="rule"></span></h2>
    <div class="feature" style="top:56px">
      <h3><svg width="12" height="14" viewBox="0 0 12 14"><circle cx="6" cy="5" r="4" fill="none" stroke="var(--green)" stroke-width="1.6"/><path d="M3,8 L2,13 L6,11 L10,13 L9,8" fill="none" stroke="var(--green)" stroke-width="1.4"/></svg>30 YEARS TRUSTED EXPERIENCE</h3>
      <p>Proudly serving all Southern Nevada based real estate companies</p>
    </div>
    <div class="feature" style="top:114px">
      <h3><svg width="14" height="13" viewBox="0 0 14 13"><rect x="1" y="2" width="12" height="10" fill="none" stroke="var(--green)" stroke-width="1.5"/><path d="M3,10 L6,6 L9,9 L11,7" fill="none" stroke="var(--green)" stroke-width="1.3"/></svg>PROFESSIONAL PHOTOS</h3>
      <ul>
        <li>Properties with quality photos sell 32% faster!</li>
        <li>Stand out against the competition.</li>
        <li>Up to 20% higher asking price per sq. ft.</li>
      </ul>
    </div>
    <div class="feature" style="top:204px">
      <h3><svg width="14" height="12" viewBox="0 0 14 12"><rect x="1" y="1" width="12" height="10" fill="none" stroke="var(--green)" stroke-width="1.5"/><path d="M2,10 L6,5 L9,8 L12,5" fill="none" stroke="var(--green)" stroke-width="1.3"/></svg>STUNNING AERIAL IMAGES</h3>
      <p>Take your listings to the next level and show case your listings like never before!</p>
    </div>
    <div class="photo" style="top:258px;height:132px;background:linear-gradient(135deg,#e7d8c4 0%,#b86a2e 40%,#3a3430 75%,#c9b79c 100%)" role="img" aria-label="Kitchen with wood cabinets and granite island"></div>
    <div class="photo" style="top:392px;height:148px;background:linear-gradient(135deg,#5a3a24 0%,#caa27a 45%,#8a5a36 75%,#e3cfb4 100%)" role="img" aria-label="Master bathroom with marble tub and onyx wall"></div>
  </div>

  <div class="panel p2 best">
    <div class="top-band" style="background:var(--orange)"></div>
    <h2 class="heading">WHAT MAKES US<br><span class="green">THE BEST?</span></h2>
    <p class="body-copy" style="top:84px">We bring the highest quality photography in a simple, elegant way. We'll handle making it look beautiful, so all you have to worry about is capturing more leads, winning more listing, and selling more properties.</p>
    <div class="photo" style="top:148px;height:108px;background:linear-gradient(135deg,#d9c7a8 0%,#9b5a2c 45%,#4a3a30 70%,#d98a4a 100%)" role="img" aria-label="Open kitchen and dining area with orange chairs"></div>
    <div class="howto"><svg width="16" height="16" viewBox="0 0 16 16"><rect x="1" y="1" width="14" height="14" fill="none" stroke="var(--green)" stroke-width="1.3"/><path d="M3,5 L4.5,6.5 L7,4 M3,10 L4.5,11.5 L7,9 M9,5.5 H13 M9,10.5 H13" fill="none" stroke="var(--green)" stroke-width="1.2"/></svg>HOW WE DO IT</div>
    <p class="body-copy" style="top:302px">Our trained real estate photographers will capture all interior/exterior views including amenities of your property.</p>
    <p class="body-copy" style="top:341px">We use only the best cameras and optics available to produce results that make your property stand out and give buyers a sense of quality and attention to detail.</p>
  </div>

  <div class="panel p3 tech">
    <div class="top-band" style="background:var(--green)"></div>
    <h3><svg width="18" height="18" viewBox="0 0 18 18"><circle cx="7" cy="10" r="4" fill="none" stroke="var(--green)" stroke-width="1.6" stroke-dasharray="2.2 1.2"/><circle cx="13" cy="4" r="2.6" fill="none" stroke="var(--green)" stroke-width="1.4" stroke-dasharray="1.6 1"/></svg>BRIGHTLENS TECHNOLOGY</h3>
    <p class="body-copy" style="left:10px;top:59px;font-size:8.3px">Take your listings to the next level with our unique HDR BRIGHTLENS Technology. Our process digitally enhances the image through an augmentation process. The end result is sharper photos, enhanced colors and elimination of overexposed windows.</p>
    <div class="photo" style="top:148px;height:262px;width:120px;background:linear-gradient(180deg,#d8d8d8 0%,#c4c4c4 45%,#6a5446 70%,#3e3028 100%)" role="img" aria-label="Empty room before enhancement"></div>
    <div class="photo" style="left:120px;top:148px;height:262px;width:112px;background:linear-gradient(180deg,#e6e6e6 0%,#7fa2c8 40%,#5c4a3e 70%,#3a2e26 100%)" role="img" aria-label="Same room after enhancement with clear window views"></div>
    <span class="ba-label" style="left:34px">Before</span>
    <span class="ba-label" style="left:151px">After</span>
  </div>

  <div class="includes">
    <svg class="swoosh" width="464" height="540" viewBox="0 0 464 540" aria-hidden="true">
      <path d="M0,398 Q200,376 464,378 L464,540 L0,540Z" fill="var(--green)"/>
      <path d="M0,410 Q200,386 464,390 L464,540 L0,540Z" fill="var(--orange)"/>
      <path d="M0,415 Q200,392 464,396 L464,540 L0,540Z" fill="var(--blue-deep)"/>
    </svg>
    <div class="includes-title"><i></i>ALL PHOTOGRAPHY TOURS INCLUDE:<i></i></div>
    <ul class="includes-list" style="left:10px">
      <li><svg width="16" height="13" viewBox="0 0 16 13"><rect x="1" y="3" width="14" height="9" rx="1" fill="none" stroke="var(--orange)" stroke-width="1.4"/><circle cx="8" cy="7.5" r="2.5" fill="none" stroke="var(--orange)" stroke-width="1.3"/><rect x="5" y="1" width="5" height="2" fill="var(--orange)"/></svg>High Quality Professional Photography</li>
      <li><svg width="18" height="13" viewBox="0 0 18 13"><rect x="1" y="2" width="10" height="7" fill="none" stroke="var(--orange)" stroke-width="1.4"/><path d="M11,4 H15 L17,7 V9 H11" fill="none" stroke="var(--orange)" stroke-width="1.4"/><circle cx="5" cy="11" r="1.5" fill="var(--orange)"/><circle cx="14" cy="11" r="1.5" fill="var(--orange)"/></svg>Next Day Turnaround</li>
      <li><svg width="16" height="14" viewBox="0 0 16 14"><rect x="1" y="1" width="14" height="9" fill="none" stroke="var(--orange)" stroke-width="1.4"/><path d="M8,10 V13 M5,13 H11" stroke="var(--orange)" stroke-width="1.4"/></svg>Client Portal for 24 Hour Access</li>
    </ul>
    <ul class="includes-list" style="left:256px">
      <li><svg width="16" height="16" viewBox="0 0 16 16"><path d="M10,2 L11.5,7 L16,8.5 L11.5,10 L10,15 L8.5,10 L4,8.5 L8.5,7Z" fill="var(--orange)"/><path d="M3,1 L3.7,3 L5.5,3.7 L3.7,4.4 L3,6.4 L2.3,4.4 L0.5,3.7 L2.3,3Z" fill="var(--orange)"/></svg>100% Satisfaction Guaranteed</li>
      <li><svg width="16" height="14" viewBox="0 0 16 14"><path d="M1,7 L8,1 L15,7 M3,6 V13 H13 V6" fill="none" stroke="var(--orange)" stroke-width="1.4"/><rect x="6.5" y="8.5" width="3" height="4.5" fill="var(--orange)"/></svg>Professional Studio Editing</li>
      <li><svg width="16" height="16" viewBox="0 0 16 16"><rect x="4" y="1" width="9" height="14" rx="1.5" fill="none" stroke="var(--orange)" stroke-width="1.4"/></svg>Mobile Friendly Online Gallery</li>
    </ul>
  </div>
</section>

</body>
</html>
```